Professional Services/Construction Management (Millwork) Biz Cards

We've decided on a logo and have our color palette set, now we want to design some very professional looking cards that make a strong first impression - they'll reflect our tagline (that we're going to put on the back: Innovative. Professional. Leaders.

The example business card shows generally the direction we've been thinking of going for the back side - **but we're open to other ideas**

Target Market(s)

The cards should target more high-end (wealthy) owners and general contracting companies. We want them to convey a strong first impression - in a professional and not garish way.

Industry/Entity Type

Construction Company

Contact Information for Business Card

There needs to be a place for our company contractor's license number and business address. We want to also have people's names, titles, phone number, email address. The back can be the logo, tagline and web address

Requirements
Must have
• follow our color palette
Nice to have
• Font & Styles should compliment the Harbor Joinery fonts, but not necessarily match exactly

```html
<!DOCTYPE html>
<html lang="en">
<head>
<meta charset="utf-8">
<title>Harbor Joinery Business Cards</title>
<link rel="stylesheet" href="https://fonts.googleapis.com/css2?family=Open+Sans:ital,wght@0,400;0,600;0,700;1,700&display=swap">
<style>
  :root {
    --stage: #3b3330;
    --card: #1b1b1b;
    --card-edge: #0f0f0f;
    --white: #f2f2f2;
    --olive: #8c7b50;
    --green: #5fa52f;
    --taupe: #8b7a72;
    --silver: #9a9a9a;
    --rule: #7a7a7a;
  }
  * { box-sizing: border-box; margin: 0; padding: 0; }
  html, body { width: 1200px; height: 814px; overflow: hidden; }
  body {
    background: var(--stage);
    font-family: "Open Sans", Arial, sans-serif;
    position: relative;
  }
  .card {
    position: absolute;
    width: 520px;
    height: 297px;
    background: var(--card);
    border: 1px solid var(--card-edge);
    box-shadow: 0 10px 24px rgba(0,0,0,.45);
  }
  .card-back { left: 70px; top: 140px; }
  .card-front { left: 610px; top: 380px; }

  /* Back */
  .back-brand {
    position: absolute;
    left: 0; right: 0; top: 48px;
    display: flex; flex-direction: column; align-items: center; gap: 10px;
  }
  .back-brand .mark {
    width: 110px; height: 110px; border-radius: 50%;
    background: var(--silver);
  }
  .back-brand .brand-name {
    color: var(--silver); font-weight: 700; font-size: 20px; letter-spacing: .5px;
  }
  .tagline {
    position: absolute; left: 38px; bottom: 40px;
    color: var(--white); font-style: italic; font-weight: 700; font-size: 17px;
  }

  /* Front */
  .front-brand {
    position: absolute; left: 230px; top: 26px; width: 150px;
    display: flex; flex-direction: column; align-items: center; gap: 8px;
  }
  .front-brand .mark {
    width: 92px; height: 92px; border-radius: 50%; background: var(--taupe);
  }
  .front-brand .brand-name {
    color: var(--green); font-weight: 700; font-size: 16px; white-space: nowrap;
  }
  .identity {
    position: absolute; right: 290px; top: 168px; text-align: right;
    font-size: 14px; line-height: 1.35; color: var(--white);
  }
  .identity .person { color: var(--olive); font-weight: 600; font-size: 17px; }
  .identity .title { color: var(--green); }
  .divider {
    position: absolute; left: 246px; top: 166px; width: 1px; height: 100px;
    background: var(--rule);
  }
  .contact {
    position: absolute; left: 262px; top: 170px;
    list-style: none; font-size: 14px; line-height: 1.62; color: var(--white);
  }
  .contact li { display: flex; align-items: center; gap: 8px; }
  .contact svg { width: 12px; height: 12px; fill: var(--silver); flex: none; }
</style>
</head>
<body>
  <section class="card card-back">
    <div class="back-brand">
      <div class="mark"></div>
      <div class="brand-name">Harbor Joinery</div>
    </div>
    <p class="tagline">Innovative. Professional. Leaders.</p>
  </section>

  <section class="card card-front">
    <div class="front-brand">
      <div class="mark"></div>
      <div class="brand-name">Harbor Joinery</div>
    </div>
    <div class="identity">
      <div class="person">Daniel Reyes</div>
      <div class="title">CEO/Founder</div>
      <div>412 Cedar Hollow Rd</div>
      <div>Juneau, Alaska 99801</div>
    </div>
    <div class="divider"></div>
    <ul class="contact">
      <li>lic number 40721856</li>
      <li><svg viewBox="0 0 24 24"><path d="M6.6 10.8a15 15 0 0 0 6.6 6.6l2.2-2.2a1 1 0 0 1 1-.25 11.4 11.4 0 0 0 3.6.57 1 1 0 0 1 1 1V20a1 1 0 0 1-1 1A17 17 0 0 1 3 4a1 1 0 0 1 1-1h3.5a1 1 0 0 1 1 1c0 1.25.2 2.45.57 3.57a1 1 0 0 1-.25 1z"/></svg>555 218 4460</li>
      <li><svg viewBox="0 0 24 24"><path d="M2 5h20v14H2z M4 7v.5l8 5 8-5V7l-8 5z" fill-rule="evenodd"/></svg>info@harborjn.com</li>
      <li><svg viewBox="0 0 24 24"><circle cx="12" cy="12" r="10"/></svg>www.harborjn.com</li>
    </ul>
  </section>
</body>
</html>
```